'Velunor' Nutritional supplements label design (UPDATED)

- 'Velunor' is a upscale health supplements brand
-The company will be packing the products in plastic bottles like other supplements
-Try to use a distinct design which is recognizable from distance
-Brand Logo is attached

-UPDATE- 2-

Label Dimensions and Design:

Hi Everyone,

Sorry for the late response caused by some very busy schedule.

Anyhow, here are the dimensions of the label (Self Adhesive) that we need:

Length of Label : 18cm
Height of Label : 6.5 cm

Product Names:

-Metabolism Formula
-Complete Multivitamins and Minerals (For Men, Women and Kids)
-Healthy Bones
-Skin Support
-Omega-3 oil for Healthy Heart

As for the ingredients just use Lorem Ipsum for now.

Many thanks to all of you in advance.

Target Market(s)

Middle Income families

Industry/Entity Type

Plastic

Requirements
Must have
• -Quality
-Effective
-Unique

```html
<!DOCTYPE html>
<html lang="en">
<head>
<meta charset="utf-8">
<title>Velunor – Complete Multivitamins &amp; Minerals Label</title>
<link rel="stylesheet" href="https://fonts.googleapis.com/css2?family=Alfa+Slab+One&family=Arimo:wght@400;700&family=Tinos:ital,wght@1,700&display=swap">
<style>
  :root{
    --sun-core:#fffdf2;
    --sun-mid:#ffe566;
    --sun-edge:#f7a81b;
    --label-red:#e3141b;
    --deep-red:#b10c10;
    --ink:#111111;
    --royal-blue:#1b1fa8;
    --tag-yellow:#fff21a;
    --tag-border:#d8a400;
    --brand-teal:#17b3c4;
    --produce-green:#7aa640;
    --produce-red:#c8322a;
    --produce-orange:#f08a2a;
  }
  *{margin:0;padding:0;box-sizing:border-box}
  html,body{width:1200px;height:433px;overflow:hidden;background:#ffffff}
  .label{
    position:relative;width:1200px;height:433px;overflow:hidden;
    background:
      radial-gradient(ellipse 420px 300px at 560px 250px, var(--sun-core) 0%, var(--sun-mid) 45%, rgba(255,229,102,0) 100%),
      radial-gradient(ellipse 900px 520px at 560px 230px, #ffd43a 0%, var(--sun-edge) 100%);
    font-family:"Arimo", Arial, sans-serif;
  }
  .produce-photo{
    position:absolute;right:0;top:0;width:440px;height:433px;
    background:
      radial-gradient(circle at 75% 12%, var(--produce-red) 0%, rgba(200,50,42,0) 30%),
      radial-gradient(circle at 90% 40%, #e9ecd8 0%, rgba(233,236,216,0) 22%),
      radial-gradient(circle at 85% 85%, #8a1c1c 0%, rgba(138,28,28,0) 28%),
      radial-gradient(circle at 70% 65%, #f2cf3a 0%, rgba(242,207,58,0) 30%),
      radial-gradient(circle at 55% 90%, #a9cf5a 0%, rgba(169,207,90,0) 25%),
      linear-gradient(160deg, var(--produce-orange) 0%, var(--produce-green) 55%, #c9a23a 100%);
    -webkit-mask-image:linear-gradient(90deg, transparent 0%, #000 40%);
    mask-image:linear-gradient(90deg, transparent 0%, #000 40%);
  }
  .count{position:absolute;left:150px;top:38px;width:110px;text-align:center;color:var(--label-red);font-weight:700}
  .count-number{
    display:inline-block;background:#fff;border-radius:12px;padding:0 9px;
    font-size:18px;line-height:20px;
  }
  .count-unit{display:block;font-size:19px;font-weight:400;line-height:22px}
  .net-weight{position:absolute;left:144px;top:112px;color:var(--ink);font-size:20px;line-height:25px}
  .title-art{position:absolute;left:0;top:0}
  .title-word{font-family:"Alfa Slab One", Georgia, serif;paint-order:stroke fill;stroke-linejoin:round}
  .audience-tag{
    position:absolute;left:390px;top:306px;width:470px;height:60px;
    background:var(--tag-yellow);border:2px solid var(--tag-border);
    box-shadow:inset 0 0 0 4px var(--tag-yellow), inset 0 0 0 5px #c99200;
    display:flex;align-items:center;justify-content:center;
    font-family:"Tinos", "Times New Roman", serif;font-style:italic;font-weight:700;color:var(--royal-blue);
  }
  .audience-for{font-size:14px;color:#c8102e;margin-right:3px;align-self:center}
  .audience-list{font-size:34px}
  .maker{position:absolute;left:60px;top:315px;width:270px}
  .maker-note{display:block;text-align:right;font-size:13px;color:var(--ink);margin-bottom:8px}
  .brand-name{display:flex;align-items:center;gap:10px;font-size:38px;font-weight:700;color:var(--brand-teal);letter-spacing:1px}
  .brand-dot{width:30px;height:30px;border-radius:50%;background:var(--brand-teal)}
</style>
</head>
<body>
<main class="label">
  <div class="produce-photo" role="img" aria-label="Photo of fresh fruits and vegetables: radishes, pears, cauliflower, bananas, grapes, apples and melon"></div>

  <div class="count">
    <span class="count-number">270</span>
    <span class="count-unit">Capsules</span>
  </div>

  <p class="net-weight">Net Weight<br>228g(8.0oz)</p>

  <svg class="title-art" width="1200" height="433" viewBox="0 0 1200 433" aria-label="Complete Multivitamins &amp; Minerals">
    <rect x="434" y="64" width="190" height="40" rx="3" fill="#3a1a00"/>
    <rect x="430" y="60" width="190" height="40" rx="3" fill="var(--tag-yellow)"/>
    <text x="525" y="91" text-anchor="middle" font-family="Arimo, Arial, sans-serif" font-weight="700" font-size="30" fill="var(--label-red)" stroke="#ffffff" stroke-width="2" paint-order="stroke fill">Complete</text>

    <text class="title-word" x="348" y="222" textLength="568" lengthAdjust="spacingAndGlyphs" font-size="148" fill="var(--deep-red)" transform="translate(4 4)">Multivitamins</text>
    <text class="title-word" x="348" y="222" textLength="568" lengthAdjust="spacingAndGlyphs" font-size="148" fill="var(--label-red)" stroke="#ffffff" stroke-width="6">Multivitamins</text>

    <text class="title-word" x="400" y="286" textLength="70" lengthAdjust="spacingAndGlyphs" font-size="70" fill="var(--label-red)" stroke="#ffffff" stroke-width="5">&amp;</text>

    <g transform="rotate(-2 743 289)">
      <text class="title-word" x="478" y="289" textLength="530" lengthAdjust="spacingAndGlyphs" font-size="108" fill="var(--deep-red)" transform="translate(4 4)">Minerals</text>
      <text class="title-word" x="478" y="289" textLength="530" lengthAdjust="spacingAndGlyphs" font-size="108" fill="var(--label-red)" stroke="#ffffff" stroke-width="6">Minerals</text>
    </g>
  </svg>

  <div class="audience-tag">
    <span class="audience-for">for</span>
    <span class="audience-list">Men, Women &amp; Kids</span>
  </div>

  <div class="maker">
    <span class="maker-note">Manufactured by:</span>
    <div class="brand-name"><span class="brand-dot"></span>Velunor</div>
  </div>
</main>
</body>
</html>
```